Professional Photography Business cards

I need business cards that include my logo which I have uploaded. I run a photography business. I am open to ideas but I would like one side to have my logo and the other side to have my contact info. I don't have a website made but I do own a website domain. I have uploaded 2 different logo color schemes. My business colors are Blue, black , and white.

Business Name
Business Phone Number
Business Email
Business Website address
Instagram

Industry/Entity Type

Professional Photography

Contact Information for Business Card

Phone Number: 555-304-7826 email: info@tkale-studio.example Instagram: @t.kalestudio website doman- www.tkale-studio.example

Requirements
Must have
• I like the idea of a business card with a full black background front and back of card. My colors must include royal blue, black, and white

```html
<!DOCTYPE html>
<html lang="en">
<head>
<meta charset="utf-8">
<title>T. Kale Photography – Business Cards</title>
<link rel="stylesheet" href="https://fonts.googleapis.com/css2?family=Arimo:wght@400;700&display=swap">
<style>
  :root {
    --bg-top: #d2d2d2;
    --bg-bottom: #a4a4a4;
    --card: #1b1b1c;
    --royal: #2b35a8;
    --royal-line: #26307f;
    --white: #ffffff;
    --emboss: #3a3a3c;
  }
  * { box-sizing: border-box; margin: 0; padding: 0; }
  html, body { width: 1200px; height: 801px; overflow: hidden; }
  body {
    background: linear-gradient(180deg, var(--bg-top), var(--bg-bottom));
    font-family: "Arimo", Arial, sans-serif;
    position: relative;
  }
  .card {
    position: absolute;
    top: 245px;
    width: 540px;
    height: 309px;
    background: var(--card);
    border-radius: 26px;
    border-bottom: 3px solid var(--royal);
    box-shadow: 0 18px 30px rgba(0,0,0,.35);
    overflow: hidden;
  }
  .card--front { left: 40px; }
  .card--back { left: 620px; }

  /* front */
  .brand {
    position: absolute;
    right: 40px;
    top: 38px;
    text-align: right;
    color: var(--white);
  }
  .brand__name { font-size: 30px; font-weight: 400; color: var(--white); }
  .brand__tag { font-size: 9px; letter-spacing: 4px; color: var(--white); margin-top: 4px; }
  .divider {
    position: absolute;
    left: 40px; right: 40px; top: 176px;
    height: 1px;
    background: var(--royal-line);
  }
  .person {
    position: absolute;
    left: 40px;
    top: 118px;
  }
  .person__name { font-size: 26px; font-weight: 700; color: var(--royal); letter-spacing: .5px; }
  .person__role { font-size: 15px; color: var(--white); margin-top: 2px; }
  .contact {
    position: absolute;
    top: 200px;
    list-style: none;
    font-size: 15px;
    color: var(--white);
  }
  .contact li { display: flex; align-items: center; gap: 9px; margin-bottom: 12px; }
  .contact--left { left: 40px; }
  .contact--right { right: 40px; text-align: right; }
  .contact--right li { justify-content: flex-end; }
  .contact svg { flex: none; }

  /* back */
  .mark {
    position: absolute;
    inset: 0;
    display: flex;
    align-items: center;
    justify-content: center;
    gap: 16px;
    color: var(--emboss);
  }
  .mark__dot {
    width: 58px; height: 58px;
    border-radius: 50%;
    background: var(--emboss);
  }
  .mark__name { font-size: 40px; font-weight: 400; color: var(--emboss); }
</style>
</head>
<body>
  <section class="card card--front">
    <div class="brand">
      <div class="brand__name">T. Kale</div>
      <div class="brand__tag">PHOTOGRAPHY</div>
    </div>

    <div class="person">
      <div class="person__name">DANA WELLS</div>
      <div class="person__role">Managing Director</div>
    </div>

    <div class="divider"></div>

    <ul class="contact contact--left">
      <li>
        <svg width="12" height="12" viewBox="0 0 24 24" aria-hidden="true"><path fill="#2b35a8" d="M6.6 10.8a15.1 15.1 0 0 0 6.6 6.6l2.2-2.2c.3-.3.7-.4 1-.2 1.1.4 2.3.6 3.6.6.6 0 1 .4 1 1V20c0 .6-.4 1-1 1A17 17 0 0 1 3 4c0-.6.4-1 1-1h3.5c.6 0 1 .4 1 1 0 1.3.2 2.5.6 3.6.1.3 0 .7-.2 1z"/></svg>
        555-304-7826
      </li>
      <li>
        <svg width="13" height="10" viewBox="0 0 26 20" aria-hidden="true"><rect x="1" y="1" width="24" height="18" rx="2" fill="none" stroke="#2b35a8" stroke-width="2"/><path d="M1 2l12 9 12-9" fill="none" stroke="#2b35a8" stroke-width="2"/></svg>
        info@tkale-studio.example
      </li>
    </ul>

    <ul class="contact contact--right">
      <li>
        www.tkale-studio.example
        <svg width="11" height="11" viewBox="0 0 20 20" aria-hidden="true"><circle cx="10" cy="10" r="9" fill="#2b35a8"/></svg>
      </li>
      <li>
        @t.kalestudio
        <svg width="11" height="11" viewBox="0 0 20 20" aria-hidden="true"><rect x="1" y="1" width="18" height="18" rx="4" fill="#2b35a8"/></svg>
      </li>
    </ul>
  </section>

  <section class="card card--back">
    <div class="mark">
      <span class="mark__dot"></span>
      <span class="mark__name">T. Kale Photography</span>
    </div>
  </section>
</body>
</html>
```